FULLY CUSTOM MAIN BANNER IMAGE FOR MY WEBSITE-REDESIGN CURRENT

SIZE MUST BE: 1800x829

LOOKING FOR A FULLY CUSTOM MAIN BANNER IMAGE TO BE DESIGNED FOR MY NEW WEBSITE HOMEPAGE http://pixelquarry-demo.net/qa/dorin/vtl_draft/index.html THE CONTENT THAT YOU SEE ON THE UPLOADED FILE OR HERE http://pixelquarry-demo.net/qa/dorin/vtl_draft/index.html YOU CAN SEE MY EXISTING BANNER IMAGE...IS THE SAME CONTENT I WANT ON THE CUSTOM BANNER IMAGE BUT I WANT THE BANNER IMAGE TO USE IMAGES TO PORTRAY WHAT THE CONTENT SAYS. POSSIBLE INTEGRATE AN INFOGRAPHIC DESIGN IN THE BANNER IMAGE. IM OPEN TO ALL IDEAS.

WHEN SOMEONE GOES TO MY WEBSITE, IMMEDIATELY I WANT THEM TO UNDERSTAND WHAT IT IS I DO.

MY BUSINESS PROVIDES OTHER BUSINESSES WITH THE ABILITY TO CREATE PROMOTIONAL GIVEAWAYS AND MARKETING PROMOTIONS USING GIFT VOUCHERS THAT ARE REDEEMABLE FOR FREE VACATIONS, CRUISES, ALL INCLUSIVE RESORT STAYS, TABLETS, SMARTWATCHES, DINING AND RESTAURANT INCENTIVES AND REWARDS AND MORE.

CURRENTLY THE CONTENT ON THE BANNER IMAGE IS THIS:
BOOST SALES & LEADS OVERNIGHT
BY ENTICING YOUR CUSTOMERS WITH FREE VACATION CERTIFICATES & OTHER HIGH PERCEIVED VALUE INCENTIVES

I HAVE ATTACHED A DOCUMENT WITH IMAGE ASSETTS YOU MAY REVIEW AND USE OR GET IDEAS FROM.

THE BOTTOM LINE IS MY SERVICE HELPS BUSINESSES INCREASE LEADS, CONVERSIONS, CTA, SALES, ETC WITHOUT HAVING TO INCREASE THEIR EXISTING AD SPEND. SIMPLY BY ADDING A FREE OFFER TO ALL THEIR EXISTING ADS WILL DRAMATICALLY INCREASE RESPONSE RATES. SO I WANT THIS BANNER TO REFLECT THIS SOMEHOW....MORE CUSTOMERS USING GIVEAWAYS!

Target Market(s)

B2B, SMALL BUSINESS OWNERS, ENTREPRENEURS, SOLOPRENEURS, MARKETING AGENCIES,

Industry/Entity Type

Digital Marketing

Requirements
Must have
• MUST PORTRAY THE RED CONTENT/TEXT USING IMAGES OF MY ASSETTS AND THE PORTRAY MORE CUSTOMERS---MUST BE FULLY CUSTOM

SIZE MUST BE: 1800x829
Nice to have
• USE CONTENT IN CURRENT BANNER IMAGE ALSO MAKE SURE TO USE THE FREE SAMPLE PKG BUTTON TOO.....MUST BE FULLY CUSTOM

SIZE MUST BE: 1800x829
Should not have
• MUST BE FULLY CUSTOM

SIZE MUST BE: 1800x829

```html
<!DOCTYPE html>
<html lang="en">
<head>
<meta charset="utf-8">
<title>Boost Sales &amp; Leads Overnight</title>
<link href="https://fonts.googleapis.com/css2?family=Audiowide&family=Oswald:wght@600&family=Open+Sans:wght@400;600;700&display=swap" rel="stylesheet">
<style>
  :root {
    --bg: #e9e9ea;
    --bg-light: #f4f4f5;
    --green: #3aa640;
    --green-btn: #1fa847;
    --lead-green: #3cc25e;
    --blue: #1565c0;
    --blue-dark: #0d4f9e;
    --sky-blue: #1e88e5;
    --navy: #1b2a4a;
    --red: #c62828;
    --yellow: #f5c518;
    --ink: #3f3f42;
    --rule: #58585b;
    --fine: #555559;
    --white: #ffffff;
  }
  * { margin: 0; padding: 0; box-sizing: border-box; }
  html, body { width: 1200px; height: 553px; overflow: hidden; background: var(--bg); }
  .banner { position: relative; width: 1200px; height: 553px; overflow: hidden; background: var(--bg); font-family: "Open Sans", Arial, sans-serif; }
  .backdrop { position: absolute; inset: 0; }
  .brand-mark {
    position: absolute; left: 720px; top: 360px;
    font-family: "Audiowide", sans-serif; font-size: 210px; line-height: 1;
    color: var(--white); opacity: .85;
  }

  /* Heading block */
  .headline {
    position: absolute; left: 123px; top: 64px; width: 960px;
    font-family: "Audiowide", sans-serif; font-weight: 400; font-size: 45px; line-height: 1;
    white-space: nowrap; color: var(--ink); letter-spacing: .5px;
  }
  .headline .boost { color: var(--green); font-size: 50px; }
  .headline .overnight { color: var(--blue); }
  .rule { position: absolute; left: 131px; top: 119px; width: 944px; height: 3px; background: var(--rule); }
  .subline {
    position: absolute; left: 147px; top: 127px; width: 920px;
    font-size: 17px; font-weight: 400; color: #1d1d1f; white-space: nowrap;
  }

  /* Fan of sample flyers */
  .flyers { position: absolute; left: 133px; top: 152px; width: 932px; height: 226px; }
  .card {
    position: absolute; width: 100px; overflow: hidden; background: var(--white);
    display: flex; flex-direction: column;
    box-shadow: 0 4px 9px rgba(0,0,0,.4); font-family: "Open Sans", Arial, sans-serif;
  }
  .card.left { transform-origin: left center; transform: perspective(500px) rotateY(30deg); }
  .card.right { transform-origin: right center; transform: perspective(500px) rotateY(-30deg); }
  .photo { flex: none; }

  /* Lead-capture flyer */
  .lead { background: linear-gradient(#17293a, #0b151e 75%, #15222e); padding: 12px 8px 6px; color: var(--white); }
  .lead-title { font-family: "Audiowide", sans-serif; font-size: 12px; line-height: 1.1; color: var(--lead-green); }
  .lead-copy { margin-top: 6px; font-size: 5.5px; line-height: 1.5; text-transform: uppercase; }
  .lead-offer { margin-top: 4px; font-size: 6px; font-weight: 700; line-height: 1.35; color: var(--yellow); text-transform: uppercase; }
  .field { margin-top: 4px; height: 13px; background: var(--white); color: #8a8a8e; font-size: 5.5px; line-height: 13px; padding-left: 4px; }
  .submit { margin-top: 5px; height: 13px; background: var(--sky-blue); color: var(--white); font-size: 6px; font-weight: 700; line-height: 13px; text-align: right; padding-right: 8px; }
  .lead-foot { margin-top: auto; font-size: 5px; line-height: 1.35; font-style: italic; }

  /* Voucher flyer */
  .voucher { padding-bottom: 4px; }
  .v-head { display: flex; align-items: flex-end; gap: 3px; padding: 6px 6px 0; }
  .enjoy { font-family: "Oswald", sans-serif; font-weight: 600; font-size: 19px; line-height: 1; color: var(--navy); }
  .v-tagset { display: flex; flex-direction: column; align-items: flex-start; padding-bottom: 2px; }
  .v-kicker { font-size: 4.5px; font-weight: 700; color: var(--navy); text-transform: uppercase; }
  .tag { background: var(--red); color: var(--white); font-family: "Oswald", sans-serif; font-weight: 600; font-size: 7px; line-height: 1.25; padding: 0 2px; }
  .v-sub { padding: 2px 6px 3px; font-size: 5.2px; line-height: 1.3; color: var(--sky-blue); font-weight: 600; }
  .band { background: var(--red); color: var(--white); font-size: 4.2px; font-weight: 700; line-height: 7px; padding-left: 6px; white-space: nowrap; }
  .fine { padding: 3px 6px 0; font-size: 3.8px; line-height: 1.4; color: var(--fine); }
  .label { margin: 3px 6px 0; align-self: flex-start; background: var(--navy); color: var(--white); font-size: 4px; font-weight: 700; line-height: 6px; padding: 0 3px; }
  .how { padding: 3px 6px 0; font-size: 4.5px; font-weight: 700; color: var(--red); }
  .v-foot { margin-top: auto; display: flex; justify-content: space-between; align-items: flex-end; padding: 0 6px; gap: 3px; }
  .cert-id { font-size: 4.5px; color: var(--fine); line-height: 1.3; }
  .cert-id b { color: var(--red); display: block; }
  .site { font-size: 6px; font-weight: 700; color: var(--red); white-space: nowrap; }

  /* Featured certificate */
  .featured { left: 392px; top: 28px; width: 150px; height: 197px; z-index: 20; }
  .featured .v-head { padding: 7px 7px 0; }
  .featured .enjoy { font-size: 24px; }
  .featured .v-kicker { font-size: 5px; }
  .featured .tag { font-size: 9px; }
  .featured .v-sub { font-size: 6px; padding: 3px 7px 2px; }
  .sponsor { position: absolute; right: 5px; top: 5px; width: 40px; text-align: center; color: #7a7a7e; font-size: 3.8px; line-height: 1.3; }
  .sponsor-name { display: flex; align-items: center; justify-content: center; gap: 2px; font-size: 8px; font-weight: 700; line-height: 1.2; }
  .sponsor-name i { width: 5px; height: 5px; background: #9a9a9e; display: block; }
  .circles { position: absolute; right: 4px; top: 68px; display: flex; flex-direction: column; gap: 4px; }
  .circle { width: 27px; height: 27px; border-radius: 50%; border: 2px solid var(--red); box-shadow: 0 0 0 1.5px var(--white) inset; }
  .featured .fine, .featured .how, .featured .label { margin-right: 34px; }
  .features { display: grid; grid-template-columns: 1fr 1fr; gap: 0 4px; padding: 2px 34px 0 7px; font-size: 3.6px; line-height: 1.45; color: var(--fine); }
  .features span::before { content: "\2713  "; color: var(--red); font-weight: 700; }
  .featured .v-foot { border-top: 1px solid #ddd; padding-top: 3px; margin: auto 6px 0; padding-left: 0; padding-right: 0; }
  .redeem { text-align: center; font-size: 3.8px; font-weight: 700; color: var(--navy); line-height: 1.35; }
  .redeem .site { display: block; font-size: 7px; }
  .terms { font-size: 3px; font-weight: 400; color: var(--fine); }

  /* Right-hand certificates and collages */
  .cert { padding-bottom: 4px; }
  .cert .sponsor { width: 34px; }
  .cert .sponsor-name { font-size: 7px; }
  .cert .tag { position: absolute; left: 4px; top: 8px; font-size: 6px; }
  .cert .circles { top: 52px; right: 3px; gap: 3px; }
  .cert .circle { width: 22px; height: 22px; }
  .cert .fine { margin-right: 26px; }
  .cert .site { padding: 0 5px; }
  .collage { background: var(--white); }

  /* Offer line and button */
  .offer {
    position: absolute; left: 259px; top: 388px; width: 700px;
    font-family: "Audiowide", sans-serif; font-size: 24px; color: var(--ink); white-space: nowrap;
  }
  .offer .get, .offer .limited { color: var(--blue); }
  .offer .free { color: var(--green); font-size: 35px; }
  .cta { position: absolute; left: 432px; top: 440px; width: 336px; height: 77px; background: var(--green-btn); border-radius: 4px; box-shadow: 0 4px 6px rgba(0,0,0,.2); text-decoration: none; }
  .cta-tab { position: absolute; left: 445px; top: 428px; width: 80px; height: 112px; }
  .cta-title { position: absolute; right: 13px; top: 14px; font-family: "Audiowide", sans-serif; font-size: 18.5px; color: var(--white); white-space: nowrap; }
  .cta-note { position: absolute; right: 13px; top: 42px; font-size: 15px; font-weight: 600; color: var(--white); }
</style>
</head>
<body>
<main class="banner">
  <svg class="backdrop" width="1200" height="553" viewBox="0 0 1200 553" aria-hidden="true">
    <polygon points="0,0 560,0 330,553 0,553" fill="var(--bg-light)"/>
    <polygon points="980,0 1200,0 1200,553 760,553" fill="#e2e2e4"/>
    <polygon points="1080,0 1200,0 1200,20 1133,120" fill="var(--blue)"/>
    <polygon points="60,427 127,553 0,553 0,540" fill="var(--blue)"/>
    <polygon points="0,470 40,553 0,553" fill="var(--blue-dark)"/>
  </svg>
  <div class="brand-mark" aria-hidden="true">VTL</div>

  <h1 class="headline"><span class="boost">BOOST</span> SALES &amp; LEADS <span class="overnight">OVERNIGHT</span></h1>
  <div class="rule"></div>
  <p class="subline">BY ENTICING YOUR CUSTOMERS WITH FREEVACATION CERTIFICATES &amp; OTHER HIGHPERCEIVED VALUE INCENTIVES</p>

  <div class="flyers">
    <!-- Left fan -->
    <section class="card left lead" style="left:0;top:3px;height:205px;z-index:1">
      <p class="lead-title">WANT A<br>GREAT OFFER?</p>
      <p class="lead-copy">Subscribe to our newsletter<br>Receive a complimentary</p>
      <p class="lead-offer">Two night getaway<br>Viva Las Vegas!</p>
      <div class="field">Name</div><div class="field">Email</div><div class="field">Phone</div>
      <div class="submit">SUBMIT</div>
      <p class="lead-foot">We will send an email and a text with the offer and instructions on how to redeem</p>
    </section>

    <section class="card left voucher" style="left:67px;top:8px;height:200px;z-index:2">
      <div class="v-head"><span class="enjoy">ENJOY</span><span class="v-tagset"><span class="v-kicker">Airfare with</span><span class="tag">2 NIGHTS</span></span></div>
      <p class="v-sub">Two Roundtrip Airfare with<br>2 Nights Hotel Accommodations</p>
      <div class="photo" role="img" aria-label="Airliner flying over clouds" style="height:42px;background:linear-gradient(#eaf2fb,#9ec5ea 60%,#d7e6f4)"></div>
      <div class="band">EXCLUSIVELY FOR : CUSTOMER NAME</div>
      <p class="fine">Two roundtrip airfares for two guests included. Hotel stay at a top destination of choice. Taxes and booking fees paid by sponsor.</p>
      <span class="label">FEATURES</span>
      <p class="how">HOW CAN WE DO THIS?</p>
      <p class="fine">We partner with travel suppliers who fill empty seats and rooms, so your customers enjoy real value at no cost.</p>
      <div class="v-foot"><span class="cert-id"><b>#10983-95930</b></span><span class="site">WWW.VTLREWARDS.COM</span></div>
    </section>

    <section class="card left lead" style="left:135px;top:25px;height:190px;z-index:3">
      <p class="lead-title">WANT A<br>GREAT OFFER?</p>
      <p class="lead-copy">Subscribe to our newsletter<br>Receive a complimentary</p>
      <p class="lead-offer">7 nights luxury resort<br>getaway + 3500 lodging</p>
      <div class="field">Name</div><div class="field">Email</div><div class="field">Phone</div>
      <div class="submit">SUBMIT</div>
      <p class="lead-foot">We will send an email and a text with the offer and instructions on how to redeem</p>
    </section>

    <section class="card left voucher" style="left:200px;top:31px;height:180px;z-index:4">
      <div class="v-head"><span class="enjoy">ENJOY</span><span class="v-tagset"><span class="v-kicker">Restaurant</span><span class="tag">$100 CASH</span></span></div>
      <p class="v-sub">$100 Dining Certificate<br>Participating Restaurants</p>
      <div class="photo" role="img" aria-label="Plated dinner and wine glasses in a restaurant" style="height:40px;background:linear-gradient(135deg,#6b3a22,#b8743e 50%,#e9d3b4)"></div>
      <div class="band">EXCLUSIVELY FOR : CUSTOMER NAME</div>
      <p class="fine">Two roundtrip airfares for two guests included. Hotel stay at a top destination of choice. Taxes and booking fees paid by sponsor.</p>
      <span class="label">FEATURES</span>
      <p class="how">HOW CAN WE DO THIS?</p>
      <p class="fine">We partner with travel suppliers who fill empty seats and rooms, so your customers enjoy real value at no cost.</p>
      <div class="v-foot"><span class="cert-id"><b>#10983-95930</b></span><span class="site">WWW.VTLREWARDS.COM</span></div>
    </section>

    <section class="card left lead" style="left:262px;top:40px;height:172px;z-index:5">
      <p class="lead-title">WANT A<br>GREAT OFFER?</p>
      <p class="lead-copy">Subscribe to our newsletter<br>Receive a complimentary</p>
      <p class="lead-offer">Premium true<br>wireless stereo earbuds</p>
      <div class="field">Name</div><div class="field">Email</div><div class="field">Phone</div>
      <div class="submit">SUBMIT</div>
      <p class="lead-foot">We will send an email and a text with the offer and instructions on how to redeem</p>
    </section>

    <section class="card left voucher" style="left:322px;top:43px;height:165px;z-index:6">
      <div class="v-head"><span class="enjoy">ENJOY</span><span class="v-tagset"><span class="v-kicker">Cruise</span><span class="tag">4 NIGHT</span></span></div>
      <p class="v-sub">5 Days / 4 Nights<br>Caribbean Cruise</p>
      <div class="photo" role="img" aria-label="Cruise ship on blue sea" style="height:38px;background:linear-gradient(#dbe9f6,#4a8ccf 55%,#2a5f96)"></div>
      <div class="band">EXCLUSIVELY FOR : CUSTOMER NAME</div>
      <p class="fine">Two roundtrip airfares for two guests included. Hotel stay at a top destination of choice. Taxes and booking fees paid by sponsor.</p>
      <p class="how">HOW CAN WE DO THIS?</p>
      <p class="fine">We partner with travel suppliers who fill empty seats and rooms, so your customers enjoy real value at no cost.</p>
      <div class="v-foot"><span class="cert-id"><b>#10983-95930</b></span><span class="site">WWW.VTLREWARDS.COM</span></div>
    </section>

    <!-- Featured certificate -->
    <section class="card voucher featured">
      <div class="v-head"><span class="enjoy">ENJOY</span><span class="v-tagset"><span class="v-kicker">Airfare with</span><span class="tag">2 NIGHTS</span></span></div>
      <div class="sponsor">Compliments Of<span class="sponsor-name"><i></i>LOGO</span>YOUR NAME</div>
      <p class="v-sub">Two Roundtrip Airfare with<br>2 Nights Hotel Accommodations</p>
      <div class="photo" role="img" aria-label="Airliner climbing through a blue sky above clouds" style="height:46px;background:linear-gradient(#f4f8fc,#a9cbec 55%,#e2ecf6)"></div>
      <div class="band" style="font-size:4.6px;line-height:9px">EXCLUSIVELY FOR : CUSTOMER NAME</div>
      <div class="circles">
        <div class="circle" role="img" aria-label="Traveller at an airport window" style="background:#3d4a57"></div>
        <div class="circle" role="img" aria-label="Couple relaxing on a beach" style="background:#4f9fc4"></div>
        <div class="circle" role="img" aria-label="Airliner at sunset" style="background:#8a6a5a"></div>
      </div>
      <p class="fine">Congratulations! You have received a travel certificate from your sponsor good for airfare and hotel at one of many popular destinations.</p>
      <span class="label">FEATURES</span>
      <div class="features">
        <span>Two Roundtrip Airfare</span><span>No Blackout Dates</span>
        <span>Two Nights Hotel Included</span><span>Transferable To Another Person</span>
        <span>Top Destinations</span><span>Valid For 18 Months</span>
        <span>Flights From Major Airports</span><span>Redeem Online Anytime</span>
      </div>
      <p class="how">HOW CAN WE DO THIS?</p>
      <p class="fine">We partner with travel suppliers who fill empty seats and rooms, so your customers enjoy real value at no cost.</p>
      <div class="v-foot">
        <span class="cert-id">Certificate ID<b>#10983-95930</b>Expires 02/28/2020</span>
        <span class="redeem">VIEW ALL THE DETAILS OF<br>THIS SPECIAL OFFER AND REDEEM ONLINE AT<span class="site">WWW.VTLREWARDS.COM</span><span class="terms">Terms and conditions apply, see redemption site for details</span></span>
      </div>
    </section>

    <!-- Right fan -->
    <section class="card right cert" style="right:325px;top:47px;height:161px;z-index:12">
      <div class="photo" role="img" aria-label="Beachfront resort hotels" style="height:44px;background:linear-gradient(#cfe5f5,#6fb1d8 60%,#d9c7a8)"></div>
      <span class="tag">RESORT CREDITS</span>
      <div class="sponsor">Compliments Of<span class="sponsor-name"><i></i>LOGO</span>YOUR NAME</div>
      <div class="band">EXCLUSIVELY FOR : CUSTOMER NAME</div>
      <div class="circles">
        <div class="circle" role="img" aria-label="Resort pool" style="background:#3fa0c8"></div>
        <div class="circle" role="img" aria-label="Hotel room" style="background:#b89a78"></div>
        <div class="circle" role="img" aria-label="Beach at dusk" style="background:#c0704a"></div>
      </div>
      <p class="fine">Two roundtrip airfares for two guests included. Hotel stay at a top destination of choice. Taxes and booking fees paid by sponsor.</p>
      <div class="v-foot"><span class="site">WWW.VTLREWARDS.COM</span></div>
    </section>

    <section class="card right collage" role="img" aria-label="Collage of smartwatch close-ups and people exercising" style="right:262px;top:41px;height:167px;z-index:11;background:linear-gradient(160deg,#d9d9d9,#7d838b 35%,#f2f2f2 50%,#8f959c 70%,#d6d6d6)"></section>

    <section class="card right cert" style="right:202px;top:35px;height:173px;z-index:10">
      <div class="photo" role="img" aria-label="Woman checking a smartwatch after a workout" style="height:48px;background:linear-gradient(#efefef,#c0c4c8 60%,#9aa0a6)"></div>
      <span class="tag">SMARTWATCH</span>
      <div class="sponsor">Compliments Of<span class="sponsor-name"><i></i>LOGO</span>YOUR NAME</div>
      <div class="band">EXCLUSIVELY FOR : CUSTOMER NAME</div>
      <div class="circles">
        <div class="circle" role="img" aria-label="Runner stretching" style="background:#9aa4ad"></div>
        <div class="circle" role="img" aria-label="Watch on a wrist" style="background:#6d6258"></div>
        <div class="circle" role="img" aria-label="Fitness tracker close-up" style="background:#a08a78"></div>
      </div>
      <p class="fine">Two roundtrip airfares for two guests included. Hotel stay at a top destination of choice. Taxes and booking fees paid by sponsor.</p>
      <div class="v-foot"><span class="site">WWW.VTLREWARDS.COM</span></div>
    </section>

    <section class="card right collage" role="img" aria-label="Collage of airport lounge and airliners at the gate" style="right:135px;top:25px;height:183px;z-index:9;background:linear-gradient(165deg,#cfe3f5,#8aa4bc 35%,#f2f2f2 50%,#7e8fa0 70%,#c7ccd2)"></section>

    <section class="card right cert" style="right:68px;top:11px;height:197px;z-index:8">
      <div class="photo" role="img" aria-label="Las Vegas strip hotels at dusk" style="height:58px;background:linear-gradient(#d8dff0,#7b86b0 55%,#3a3f66)"></div>
      <span class="tag">VEGAS NIGHTS</span>
      <div class="sponsor">Compliments Of<span class="sponsor-name"><i></i>LOGO</span>YOUR NAME</div>
      <div class="band">EXCLUSIVELY FOR : CUSTOMER NAME</div>
      <div class="circles" style="top:64px">
        <div class="circle" role="img" aria-label="Casino slot machines" style="background:#2c3566"></div>
        <div class="circle" role="img" aria-label="Hotel lobby" style="background:#a8825a"></div>
        <div class="circle" role="img" aria-label="Show stage lights" style="background:#9a2a3a"></div>
      </div>
      <p class="fine">Two roundtrip airfares for two guests included. Hotel stay at a top destination of choice. Taxes and booking fees paid by sponsor.</p>
      <div class="v-foot"><span class="site">WWW.VTLREWARDS.COM</span></div>
    </section>

    <section class="card right collage" role="img" aria-label="Collage of a cruise ship and a palm-lined tropical beach" style="right:0;top:0;height:211px;z-index:7;background:linear-gradient(160deg,#8fc7ef,#d8dfe5 35%,#f4f4f4 48%,#5ba4c8 65%,#e8d9b8)"></section>
  </div>

  <p class="offer"><span class="get">GET</span> <span class="free">FREE</span> SAMPLES NOW FOR A <span class="limited">LIMITED TIME !</span></p>

  <a class="cta" href="#samples">
    <span class="cta-title">GET FREE SAMPLES</span>
    <span class="cta-note">100% FREE</span>
  </a>
  <svg class="cta-tab" viewBox="0 0 80 112" aria-hidden="true">
    <polygon points="0,0 80,0 80,98 40,112 0,98" fill="var(--white)"/>
    <polygon points="0,92 40,104 80,92 80,100 40,112 0,100" fill="var(--blue)"/>
    <g fill="none" stroke="var(--blue)" stroke-width="5" stroke-linecap="square">
      <polyline points="28,26 40,37 52,26"/>
      <polyline points="28,42 40,53 52,42"/>
      <polyline points="28,58 40,69 52,58"/>
    </g>
  </svg>
</main>
</body>
</html>
```